New E-Learning Website Design Wanted!

I am creating an E-learning website for those interested in getting certifications in the IT industry.
For example, courses related to BKX, Pellin, RTM certifications and national certifications in the IT industry in Japan will be offered.
You can think of sites such as Pindoval, Fevly, VexaPoint, Bintorum.
But I am targeting industries in Japan at the moment.
Also, I have uploaded screenshots of pages that I think are good.

The company is Solvik Data
I recently got my company logo designed so I attached pdf file to this project brief.
I would appreciate it if you can make the site match the color scheme of the logo.

Target Market(s)

I am targeting individuals as well as large IT companies in Japan

Industry/Entity Type

Education

Coding

Coded - Design and coding required

Number of Pages Required

4 page

Font styles to use
Sans Serif

Colors

Designer to choose colors to be used in the design.

Requirements
Must have
• One top page design
• One course page (https://vexapt.test/courses/pellor-grid-systems)
• One learning page(where the learner can see the video)
• One blog page(https://news.vexapt.test/resources?_ga=2.36414185.89678801.1578174478-594719062.1578174478)
Nice to have
• Pricing page

```html
<!DOCTYPE html>
<html lang="en">
<head>
<meta charset="utf-8">
<title>Solvik Data – Online IT Courses</title>
<link href="https://fonts.googleapis.com/css2?family=Archivo:wght@500;600;700&family=Lato:ital,wght@0,400;0,700;1,400&display=swap" rel="stylesheet">
<style>
:root{
  --navy:#172a5c;
  --navy-deep:#101f4a;
  --ink:#1a2447;
  --teal:#22b1c4;
  --teal-soft:#cfeef2;
  --mist:#e0ecee;
  --text:#4a5a78;
  --muted:#7b879d;
  --orange:#f7a600;
  --white:#ffffff;
  --line:#e3e7ee;
}
*{box-sizing:border-box;margin:0;padding:0}
html,body{width:1200px;height:4461px;overflow:hidden}
body{position:relative;background:var(--white);font-family:"Lato",sans-serif;color:var(--text)}
.abs{position:absolute}
.heading{font-family:"Archivo",sans-serif;font-weight:700;color:var(--ink);text-transform:uppercase;letter-spacing:.2px}
.btn-outline{position:absolute;display:flex;align-items:center;justify-content:center;border:2px solid var(--navy);color:var(--navy);font-family:"Archivo",sans-serif;font-weight:600;font-size:14px;text-transform:uppercase}

/* hero */
.hero{position:absolute;left:0;top:0;width:1200px;height:746px;overflow:hidden}
.hero-photo{position:absolute;inset:0;background:linear-gradient(100deg,#1f3560 0%,#2a4a7c 38%,#3a5f8e 62%,#1a2d52 100%)}
.hero-shade{position:absolute;inset:0;background:linear-gradient(90deg,rgba(20,34,72,.75) 0%,rgba(20,34,72,.35) 50%,rgba(20,34,72,0) 80%)}
.brand{position:absolute;display:flex;align-items:center;gap:10px;font-family:"Lato",sans-serif;font-weight:400;color:var(--white)}
.brand-mark{width:22px;height:22px;border:2px solid currentColor;border-radius:50%}
.nav{position:absolute;top:40px;left:0;width:1200px;height:20px;font-family:"Archivo",sans-serif;font-weight:600;font-size:13.5px;color:var(--white)}
.nav span{position:absolute;top:0}
.lang{position:absolute;left:1005px;top:31px;width:74px;height:35px;border:1px solid rgba(255,255,255,.7);color:#fff;font-size:12px;display:flex;align-items:center;justify-content:center;gap:5px;font-family:"Archivo",sans-serif}
.cart-badge{position:absolute;left:954px;top:32px;width:17px;height:17px;border-radius:50%;background:#fff;color:var(--navy);font-size:10px;font-weight:700;display:flex;align-items:center;justify-content:center}
.hero-title{position:absolute;left:125px;top:282px;font-size:35px;line-height:44px;color:#fff}
.hero-copy{position:absolute;left:129px;top:378px;width:440px;font-size:17px;line-height:27px;color:rgba(255,255,255,.85)}
.hero-btn{position:absolute;left:132px;top:452px;width:197px;height:50px;border:2px solid #fff;color:#fff;font-family:"Archivo",sans-serif;font-weight:600;font-size:14px;display:flex;align-items:center;justify-content:center}
.dots span{position:absolute;left:1114px;width:13px;height:13px;border-radius:50%;background:#fff}
.dots span:first-child{background:transparent;border:2px solid #fff}

/* partners */
.partners{position:absolute;top:746px;left:0;width:1200px;height:106px;border-bottom:1px solid var(--line)}
.partner{position:absolute;top:38px;transform:translateX(-50%);font-family:"Lato",sans-serif;font-weight:700;font-size:19px;color:#8b96a3;white-space:nowrap;display:flex;align-items:center;gap:8px}
.partner i{display:block;width:14px;height:14px;background:#8b96a3}

/* why */
.why-title{position:absolute;top:918px;left:0;width:1200px;text-align:center;font-size:24px}
.why-item{position:absolute;top:988px;width:200px;height:200px;border-radius:50%;border:2px dashed var(--teal)}
.why-item .disc{position:absolute;inset:10px;border-radius:50%;display:flex;flex-direction:column;align-items:center;justify-content:center;color:#fff;font-size:17px;line-height:22px;text-align:center}
.why-item.teal .disc{background:var(--teal)}
.why-item.navy .disc{background:var(--navy)}
.why-item svg{margin-bottom:12px}

/* about */
.about{position:absolute;top:1249px;left:0;width:1200px;height:485px;background:var(--mist)}
.about-media{position:absolute;left:137px;top:91px;width:450px;height:283px;background:linear-gradient(120deg,#7e8a96,#3b4658 55%,#262d3c)}
.play{position:absolute;left:188px;top:105px;width:74px;height:74px;border-radius:50%;background:rgba(34,177,196,.85);border:4px solid rgba(255,255,255,.35);display:flex;align-items:center;justify-content:center}
.about-title{position:absolute;left:650px;top:1360px;font-size:28px}
.about-copy{position:absolute;left:650px;width:410px;font-size:14.5px;line-height:23px;color:var(--text);text-align:justify}

/* courses */
.blob{position:absolute}
.courses-title{position:absolute;left:142px;top:1808px;font-size:26px}
.course{position:absolute;top:1871px;width:293px;height:407px;background:#fff;box-shadow:0 2px 10px rgba(20,40,80,.12)}
.course-img{position:absolute;left:19px;top:16px;width:256px;height:161px}
.course h3{position:absolute;left:26px;top:197px;width:240px;font-family:"Archivo",sans-serif;font-weight:600;font-size:14px;line-height:18px;color:var(--ink)}
.course ul{position:absolute;left:26px;top:250px;list-style:none}
.course li{display:flex;align-items:center;gap:7px;font-size:11px;color:var(--muted);height:27px;white-space:nowrap}
.course .btn-outline{left:26px;top:342px;width:118px;height:33px;font-size:10.5px;border-width:2px}

/* training */
.training{position:absolute;top:2371px;left:0;width:1200px;height:544px;background:var(--mist)}
.training-title{position:absolute;left:133px;top:2492px;font-size:26px;line-height:36px}
.training-copy{position:absolute;left:134px;width:470px;font-size:14px;line-height:23px}
.dashboard{position:absolute;left:644px;top:2463px;width:428px;height:325px;background:linear-gradient(160deg,#ffffff,#eef1fb 60%,#e3e6f8);box-shadow:0 3px 14px rgba(20,40,80,.15)}

/* pricing */
.pricing-title{position:absolute;top:2990px;left:0;width:1200px;text-align:center;font-size:26px}
.plan{position:absolute;top:3067px;width:291px;height:452px;background:#fff;box-shadow:0 2px 10px rgba(20,40,80,.12)}
.plan-head{position:absolute;left:0;top:0;width:291px;height:172px;background:linear-gradient(180deg,#1f4f74,#152d55);overflow:hidden;color:#fff;text-align:center}
.plan-head h3{position:absolute;left:0;top:38px;width:100%;font-family:"Archivo",sans-serif;font-weight:600;font-size:20px}
.plan-head small{position:absolute;display:block;left:0;top:66px;width:100%;font-size:12px;letter-spacing:.5px}
.plan-head .price{position:absolute;left:0;top:98px;width:100%;font-family:"Archivo",sans-serif;font-weight:700;font-size:30px}
.plan-head .price sup{font-size:17px;vertical-align:8px}
.plan-head svg{position:absolute;left:0;bottom:0}
.plan ul{position:absolute;left:32px;top:219px;list-style:none}
.plan li{display:flex;align-items:center;gap:12px;font-size:14.5px;color:#3d5585;height:35px}
.plan-btn{position:absolute;left:26px;top:378px;width:244px;height:42px;background:var(--orange);color:#fff;font-family:"Archivo",sans-serif;font-weight:600;font-size:14px;display:flex;align-items:center;justify-content:center}

/* testimonials */
.reviews{position:absolute;top:3603px;left:0;width:1200px;height:467px;background:var(--teal)}
.reviews-title{position:absolute;top:3654px;left:0;width:1200px;text-align:center;font-size:24px;color:#fff}
.review{position:absolute;top:3760px;width:306px;height:211px;border:1px solid rgba(255,255,255,.45);text-align:center;color:#fff}
.avatar{position:absolute;left:50%;top:-42px;width:80px;height:80px;margin-left:-40px;border-radius:50%;border:3px solid #fff;background:linear-gradient(160deg,#c79a7c,#7a5544)}
.review h4{position:absolute;left:0;top:60px;width:100%;font-family:"Archivo",sans-serif;font-weight:600;font-size:14.5px}
.review p{position:absolute;top:90px;left:25px;width:256px;font-style:italic;font-size:14.5px;line-height:23px;color:rgba(255,255,255,.9)}
.arrow{position:absolute;top:3847px}

/* footer */
.footer{position:absolute;top:4070px;left:0;width:1200px;height:391px;background:var(--navy-deep)}
.footer-brand{position:absolute;left:150px;top:4228px;font-size:26px}
.social{position:absolute;top:4280px;width:20px;height:20px;border-radius:50%;border:2px solid #fff}
.f-col{position:absolute;top:4145px;color:#fff}
.f-col h5{font-family:"Archivo",sans-serif;font-weight:700;font-size:13px;margin-bottom:12px}
.f-col a{display:block;font-size:13px;line-height:28.5px;color:#a8b3cc;text-decoration:none}
.f-contact{position:absolute;display:flex;gap:10px;color:#a8b3cc;font-size:13px;line-height:19px}
.f-contact strong{display:block;font-size:16px;font-weight:400}
.f-rule{position:absolute;left:0;top:4394px;width:1200px;height:1px;background:rgba(255,255,255,.12)}
.copyright{position:absolute;top:4414px;left:0;width:1200px;text-align:center;font-size:11.5px;color:#8a96b4}
</style>
</head>
<body>

<!-- Hero -->
<section class="hero">
  <div class="hero-photo" role="img" aria-label="Young man with glasses studying at a desk, writing notes, in cool blue tones"></div>
  <div class="hero-shade"></div>
  <div class="brand" style="left:111px;top:33px;font-size:25px"><span class="brand-mark"></span>Solvik Data</div>
  <nav class="nav">
    <span style="left:421px">HOME</span>
    <span style="left:502px">LEARNING</span>
    <span style="left:613px">BLOG</span>
    <span style="left:689px">COURSE</span>
    <span style="left:788px">CERTIFICATIONS</span>
  </nav>
  <svg class="abs" style="left:938px;top:38px" width="24" height="22" viewBox="0 0 24 22" fill="none" stroke="#fff" stroke-width="1.8"><path d="M1 2h4l3 12h12l3-9H7"/><circle cx="10" cy="19" r="1.6"/><circle cx="19" cy="19" r="1.6"/></svg>
  <span class="cart-badge">0</span>
  <div class="lang">ENG <svg width="10" height="7" viewBox="0 0 10 7" fill="none" stroke="#fff" stroke-width="1.6"><path d="M1 1l4 4 4-4"/></svg></div>
  <h1 class="heading hero-title" style="color:#fff">Your online IT courses<br>to your success</h1>
  <p class="hero-copy">Maecenas aliquet velit vel turpis Mauris neque metus malesuada nec ultricies sit amet</p>
  <a class="hero-btn">GET STARTED NOW</a>
  <div class="dots">
    <span style="top:313px"></span><span style="top:335px"></span><span style="top:358px"></span><span style="top:379px"></span>
  </div>
</section>

<!-- Partners -->
<section class="partners">
  <span class="partner" style="left:204px"><i style="border-radius:50%"></i>Brevanta</span>
  <span class="partner" style="left:402px">Holdane</span>
  <span class="partner" style="left:596px">Kindred Fold</span>
  <span class="partner" style="left:793px"><i></i>Orlen Mercer</span>
  <span class="partner" style="left:987px">Platewell</span>
</section>

<!-- Why choose -->
<h2 class="heading why-title">Why choose Solvik Data</h2>
<div class="why-item teal" style="left:142px"><div class="disc">
  <svg width="56" height="50" viewBox="0 0 56 50" fill="none" stroke="#fff" stroke-width="2"><circle cx="28" cy="12" r="6"/><path d="M17 34c0-7 5-12 11-12s11 5 11 12"/><path d="M10 44h36"/><circle cx="9" cy="14" r="3"/><circle cx="47" cy="14" r="3"/><circle cx="14" cy="3" r="2"/><circle cx="42" cy="3" r="2"/></svg>
  Provide<br>Latest Skills</div></div>
<div class="why-item navy" style="left:378px"><div class="disc">
  <svg width="56" height="50" viewBox="0 0 56 50" fill="none" stroke="#fff" stroke-width="2"><path d="M6 46h44M12 46V36h10V26h10V16h10v30"/><path d="M37 16V2l10 4-10 4"/></svg>
  Get ready<br>for a career</div></div>
<div class="why-item teal" style="left:610px"><div class="disc">
  <svg width="56" height="50" viewBox="0 0 56 50" fill="none" stroke="#fff" stroke-width="2"><rect x="4" y="6" width="40" height="28" rx="2"/><path d="M16 42h16M24 34v8"/><path d="M12 16h18M12 23h12"/><circle cx="46" cy="30" r="6"/></svg>
  Easy Online<br>Learning</div></div>
<div class="why-item navy" style="left:851px"><div class="disc">
  <svg width="56" height="50" viewBox="0 0 56 50" fill="none" stroke="#fff" stroke-width="2"><path d="M12 2h24l8 8v38H12z"/><path d="M36 2v8h8"/><path d="M19 18h18M19 25h18M19 32h10"/><circle cx="36" cy="38" r="5"/></svg>
  Earn certificate<br>and degree</div></div>

<!-- About -->
<section class="about">
  <div class="about-media" role="img" aria-label="Woman writing notes beside a laptop showing an online course">
    <div class="play"><svg width="20" height="22" viewBox="0 0 20 22"><path d="M2 1l17 10L2 21z" fill="#fff"/></svg></div>
  </div>
</section>
<h2 class="heading about-title">About Solvik Data</h2>
<p class="about-copy" style="top:1412px">Etiam eleifend metus vitae adipiscing semper mauris ipsum iaculis elit congue gravida elit mi egestas orci Curabitur pede</p>
<p class="about-copy" style="top:1470px">Aliquet velit vel turpis Mauris neque metus malesuada nec ultricies sit amet porttitor mattis enim In massa libero interdum nec interdum vel blandit sed nulla In</p>
<a class="btn-outline" style="left:650px;top:1573px;width:162px;height:45px">LEARN MORE</a>

<!-- Latest courses -->
<svg class="blob" style="left:0;top:1950px" width="170" height="390" viewBox="0 0 170 390"><path d="M0 20C40 0 120 10 140 70c20 60-40 90-20 160 20 60 50 110-20 140C60 390 20 380 0 390z" fill="var(--teal)"/></svg>
<svg class="blob" style="left:920px;top:1780px" width="280" height="360" viewBox="0 0 280 360"><path d="M280 0v360c-60-10-120-70-150-130C100 170 40 150 20 110 0 60 60 40 110 60c50 20 80-30 110-50 20-12 40-14 60-10z" fill="#1b4e72"/></svg>
<h2 class="heading courses-title">Latest Courses</h2>

<article class="course" style="left:133px">
  <div class="course-img" role="img" aria-label="Hands typing code on a laptop keyboard" style="background:linear-gradient(135deg,#6b737c,#2b3038)"></div>
  <h3>Etiam eleifend metus vitae adipiscing semper mauris</h3>
  <ul>
    <li><svg width="14" height="14" viewBox="0 0 14 14" fill="none" stroke="var(--teal)" stroke-width="1.4"><circle cx="7" cy="7" r="6"/><path d="M4 7l2 2 4-4"/></svg>Maecenas aliquet velit vel turpis</li>
    <li><svg width="14" height="14" viewBox="0 0 14 14" fill="none" stroke="var(--teal)" stroke-width="1.4"><circle cx="7" cy="7" r="6"/><path d="M4 7l2 2 4-4"/></svg>Mauris neque metus malesuada nec</li>
    <li><svg width="14" height="14" viewBox="0 0 14 14" fill="none" stroke="var(--teal)" stroke-width="1.4"><circle cx="7" cy="7" r="6"/><path d="M4 7l2 2 4-4"/></svg>Amet porttitor mattis enim In massa</li>
  </ul>
  <a class="btn-outline">LEARN MORE</a>
</article>
<article class="course" style="left:457px">
  <div class="course-img" role="img" aria-label="Glowing network of data nodes on a dark blue background" style="background:linear-gradient(135deg,#1c2f8a,#1387b8 55%,#0d1a4d)"></div>
  <h3>Praesent elementum elit at<br>tellus Curabitur</h3>
  <ul>
    <li><svg width="14" height="14" viewBox="0 0 14 14" fill="none" stroke="var(--teal)" stroke-width="1.4"><circle cx="7" cy="7" r="6"/><path d="M4 7l2 2 4-4"/></svg>Maecenas aliquet velit vel turpis</li>
    <li><svg width="14" height="14" viewBox="0 0 14 14" fill="none" stroke="var(--teal)" stroke-width="1.4"><circle cx="7" cy="7" r="6"/><path d="M4 7l2 2 4-4"/></svg>Mauris neque metus malesuada nec</li>
    <li><svg width="14" height="14" viewBox="0 0 14 14" fill="none" stroke="var(--teal)" stroke-width="1.4"><circle cx="7" cy="7" r="6"/><path d="M4 7l2 2 4-4"/></svg>Amet porttitor mattis enim In massa</li>
  </ul>
  <a class="btn-outline">LEARN MORE</a>
</article>
<article class="course" style="left:783px">
  <div class="course-img" role="img" aria-label="Developer with glasses in front of screens of code" style="background:linear-gradient(135deg,#0f3a3f,#1f6d6d 50%,#0a1f24)"></div>
  <h3>Aliquam nec erat at purus<br>cursus interduma</h3>
  <ul>
    <li><svg width="14" height="14" viewBox="0 0 14 14" fill="none" stroke="var(--teal)" stroke-width="1.4"><circle cx="7" cy="7" r="6"/><path d="M4 7l2 2 4-4"/></svg>Maecenas aliquet velit vel turpis</li>
    <li><svg width="14" height="14" viewBox="0 0 14 14" fill="none" stroke="var(--teal)" stroke-width="1.4"><circle cx="7" cy="7" r="6"/><path d="M4 7l2 2 4-4"/></svg>Mauris neque metus malesuada nec</li>
    <li><svg width="14" height="14" viewBox="0 0 14 14" fill="none" stroke="var(--teal)" stroke-width="1.4"><circle cx="7" cy="7" r="6"/><path d="M4 7l2 2 4-4"/></svg>Amet porttitor mattis enim In massa</li>
  </ul>
  <a class="btn-outline">LEARN MORE</a>
</article>

<!-- Training -->
<section class="training"></section>
<h2 class="heading training-title">Spend less time<br>managing training</h2>
<p class="training-copy" style="top:2586px">Etiam eleifend metus vitae adipiscing semper mauris ipsum iaculis elit congue gravida elit mi egestas orci Curabitur pede</p>
<p class="training-copy" style="top:2644px">Aliquet velit vel turpis Mauris neque metus malesuada nec ultricies sit amet porttitor mattis enim In massa libero interdum nec</p>
<a class="btn-outline" style="left:135px;top:2719px;width:166px;height:47px">LEARN MORE</a>
<div class="dashboard" role="img" aria-label="Training analytics dashboard with charts and statistics"></div>

<!-- Pricing -->
<svg class="blob" style="left:0;top:3030px" width="150" height="240" viewBox="0 0 150 240"><path d="M0 20C60 0 140 10 140 80c0 60-60 80-80 130C40 240 20 230 0 225z" fill="var(--teal-soft)"/></svg>
<svg class="blob" style="left:1010px;top:3150px" width="190" height="320" viewBox="0 0 190 320"><path d="M190 0v320c-50-20-90-60-100-120C80 140 20 120 30 70 40 20 120 10 190 0z" fill="var(--teal-soft)"/></svg>
<h2 class="heading pricing-title">Our Pricing</h2>

<article class="plan" style="left:142px">
  <div class="plan-head"><h3>PROGRAMMING</h3><small>SUBSCRIPTION</small><div class="price"><sup>$</sup>49.99</div>
    <svg width="291" height="36" viewBox="0 0 291 36"><path d="M0 14C60 0 110 26 170 18s90-18 121-8v26H0z" fill="var(--teal)"/><path d="M0 24C70 10 120 34 180 26s80-14 111-6v16H0z" fill="#fff"/></svg></div>
  <ul>
    <li><svg width="16" height="16" viewBox="0 0 16 16"><circle cx="8" cy="8" r="8" fill="#e6f4f6"/><path d="M4.5 8l2.3 2.3 4.5-4.5" fill="none" stroke="var(--teal)" stroke-width="1.6"/></svg>Etiam eleifend metus vitae</li>
    <li><svg width="16" height="16" viewBox="0 0 16 16"><circle cx="8" cy="8" r="8" fill="#e6f4f6"/><path d="M4.5 8l2.3 2.3 4.5-4.5" fill="none" stroke="var(--teal)" stroke-width="1.6"/></svg>Adipiscing semper</li>
    <li><svg width="16" height="16" viewBox="0 0 16 16"><circle cx="8" cy="8" r="8" fill="#e6f4f6"/><path d="M4.5 8l2.3 2.3 4.5-4.5" fill="none" stroke="var(--teal)" stroke-width="1.6"/></svg>Ppsum iaculis elit congue</li>
    <li><svg width="16" height="16" viewBox="0 0 16 16"><circle cx="8" cy="8" r="8" fill="#e6f4f6"/><path d="M4.5 8l2.3 2.3 4.5-4.5" fill="none" stroke="var(--teal)" stroke-width="1.6"/></svg>Gravida elit mi egestas</li>
  </ul>
  <a class="plan-btn">GET STARTED</a>
</article>
<article class="plan" style="left:459px">
  <div class="plan-head"><h3>CLOUD</h3><small>SUBSCRIPTION</small><div class="price"><sup>$</sup>89.99</div>
    <svg width="291" height="36" viewBox="0 0 291 36"><path d="M0 14C60 0 110 26 170 18s90-18 121-8v26H0z" fill="var(--teal)"/><path d="M0 24C70 10 120 34 180 26s80-14 111-6v16H0z" fill="#fff"/></svg></div>
  <ul>
    <li><svg width="16" height="16" viewBox="0 0 16 16"><circle cx="8" cy="8" r="8" fill="#e6f4f6"/><path d="M4.5 8l2.3 2.3 4.5-4.5" fill="none" stroke="var(--teal)" stroke-width="1.6"/></svg>Etiam eleifend metus</li>
    <li><svg width="16" height="16" viewBox="0 0 16 16"><circle cx="8" cy="8" r="8" fill="#e6f4f6"/><path d="M4.5 8l2.3 2.3 4.5-4.5" fill="none" stroke="var(--teal)" stroke-width="1.6"/></svg>Adipiscing semper mauris</li>
    <li><svg width="16" height="16" viewBox="0 0 16 16"><circle cx="8" cy="8" r="8" fill="#e6f4f6"/><path d="M4.5 8l2.3 2.3 4.5-4.5" fill="none" stroke="var(--teal)" stroke-width="1.6"/></svg>Ppsum iaculis elit</li>
    <li><svg width="16" height="16" viewBox="0 0 16 16"><circle cx="8" cy="8" r="8" fill="#e6f4f6"/><path d="M4.5 8l2.3 2.3 4.5-4.5" fill="none" stroke="var(--teal)" stroke-width="1.6"/></svg>Gravida elit mi egestas</li>
  </ul>
  <a class="plan-btn">GET STARTED</a>
</article>
<article class="plan" style="left:781px">
  <div class="plan-head"><h3>ALL IN ONE</h3><small>SUBSCRIPTION</small><div class="price"><sup>$</sup>129.99</div>
    <svg width="291" height="36" viewBox="0 0 291 36"><path d="M0 14C60 0 110 26 170 18s90-18 121-8v26H0z" fill="var(--teal)"/><path d="M0 24C70 10 120 34 180 26s80-14 111-6v16H0z" fill="#fff"/></svg></div>
  <ul>
    <li><svg width="16" height="16" viewBox="0 0 16 16"><circle cx="8" cy="8" r="8" fill="#e6f4f6"/><path d="M4.5 8l2.3 2.3 4.5-4.5" fill="none" stroke="var(--teal)" stroke-width="1.6"/></svg>Etiam eleifend metus vitae</li>
    <li><svg width="16" height="16" viewBox="0 0 16 16"><circle cx="8" cy="8" r="8" fill="#e6f4f6"/><path d="M4.5 8l2.3 2.3 4.5-4.5" fill="none" stroke="var(--teal)" stroke-width="1.6"/></svg>Adipiscing semper mauris</li>
    <li><svg width="16" height="16" viewBox="0 0 16 16"><circle cx="8" cy="8" r="8" fill="#e6f4f6"/><path d="M4.5 8l2.3 2.3 4.5-4.5" fill="none" stroke="var(--teal)" stroke-width="1.6"/></svg>Ppsum iaculis elit congue</li>
    <li><svg width="16" height="16" viewBox="0 0 16 16"><circle cx="8" cy="8" r="8" fill="#e6f4f6"/><path d="M4.5 8l2.3 2.3 4.5-4.5" fill="none" stroke="var(--teal)" stroke-width="1.6"/></svg>Gravida elit mi egestas</li>
  </ul>
  <a class="plan-btn">GET STARTED</a>
</article>

<!-- Testimonials -->
<section class="reviews"></section>
<h2 class="heading reviews-title">What our students say</h2>
<svg class="arrow" style="left:92px" width="20" height="32" viewBox="0 0 20 32" fill="none" stroke="#fff" stroke-width="3"><path d="M16 3L4 16l12 13"/></svg>
<svg class="arrow" style="left:1110px" width="20" height="32" viewBox="0 0 20 32" fill="none" stroke="#fff" stroke-width="3"><path d="M4 3l12 13L4 29"/></svg>
<article class="review" style="left:139px">
  <div class="avatar" role="img" aria-label="Portrait of student Tara Bloom"></div>
  <h4>TARA BLOOM</h4>
  <p>Mauris neque metus malesuada nec ultricies sit amet porttitor mattis enim In massa libero interdum nec interdum vel blandit</p>
</article>
<article class="review" style="left:459px">
  <div class="avatar" role="img" aria-label="Portrait of student Devin Marsh"></div>
  <h4>DEVIN MARSH</h4>
  <p>Mauris neque metus malesuada nec ultricies sit amet porttitor mattis enim In massa libero interdum nec interdum vel blandit</p>
</article>
<article class="review" style="left:779px">
  <div class="avatar" role="img" aria-label="Portrait of student Nora Quill"></div>
  <h4>NORA QUILL</h4>
  <p>Mauris neque metus malesuada nec ultricies sit amet porttitor mattis enim In massa libero interdum nec interdum vel blandit</p>
</article>

<!-- Footer -->
<footer class="footer"></footer>
<div class="brand footer-brand"><span class="brand-mark"></span>Solvik Data</div>
<span class="social" style="left:186px"></span>
<span class="social" style="left:236px"></span>
<span class="social" style="left:284px"></span>
<div class="f-col" style="left:417px"><h5>COMPANY</h5><a>Home</a><a>About us</a><a>Courses</a><a>Blogs</a><a>Pricing</a></div>
<div class="f-col" style="left:568px"><h5>SERVICES</h5><a>Pellentesque</a><a>Faucibus Ut</a><a>Accumsan ultri</a><a>Non fermentum</a><a>Aec hend</a></div>
<div class="f-col" style="left:736px"><h5>RESOURCES</h5><a>Support</a><a>Sitemap</a><a>Partners</a><a>Contact</a></div>
<div class="f-col" style="left:894px"><h5>QUESTIONS</h5></div>
<div class="f-contact" style="left:893px;top:4175px">
  <svg width="20" height="20" viewBox="0 0 20 20" fill="none" stroke="#a8b3cc" stroke-width="1.5"><path d="M4 2l4 4-2 3c1 2 3 4 5 5l3-2 4 4-2 2C9 18 2 11 2 4z"/></svg>
  <div>Call Us Now<strong>(685) 555 0172</strong></div>
</div>
<div class="f-contact" style="left:893px;top:4242px">
  <svg width="20" height="16" viewBox="0 0 20 16" fill="none" stroke="#a8b3cc" stroke-width="1.5"><rect x="1" y="2" width="18" height="12"/><path d="M1 2l9 7 9-7"/></svg>
  <div>Email Us<br>info@solvikdata.test</div>
</div>
<div class="f-rule"></div>
<p class="copyright">Copyright © 2020 All right reserved</p>

</body>
</html>
```